Container Web Design Project

I need the front page of my website to have a new, fresh look.
Our company is a highly specialized marketplace for shipping containers (yes, the 20' and 40' kind). Basically, think of Quibzo for shipping containers.
I have all of the links/content that I need plugged into a wireframe (attached), and the core color (blue #0073a2) of our existing site should stay the same as we've got stationary, business cards, marketing materials...
If you have any questions please ask.

```html
<!DOCTYPE html>
<html lang="en">
<head>
<meta charset="utf-8">
<title>CargoLot – Shipping Container Marketplace</title>
<link rel="stylesheet" href="https://fonts.googleapis.com/css2?family=Roboto+Condensed:wght@300;400;700&family=Arimo:wght@400;700&display=swap">
<style>
:root{
  --brand:#0073a2;
  --brand-dark:#0a5f86;
  --brand-deep:#0c4e70;
  --link:#1670a3;
  --text:#444;
  --muted:#777;
  --line:#d6d6d6;
  --panel:#f2f2f2;
  --page:#f7f7f7;
  --white:#fff;
}
*{box-sizing:border-box;margin:0;padding:0}
html,body{width:795px;height:1200px;overflow:hidden}
body{font-family:"Arimo",Arial,sans-serif;color:var(--text);background:var(--page)}
.canvas{position:relative;width:795px;height:1200px;overflow:hidden;
  background:linear-gradient(#fff 0,#fff 110px,#e9e9e9 120px,#f4f4f4 300px,#fff 330px,#fff 1100px)}
.abs{position:absolute}
a{color:inherit;text-decoration:none}

/* header */
.masthead{left:82px;top:0;width:631px;height:46px;background:var(--brand-dark)}
.brandname{left:8px;top:6px;height:34px;padding:0 10px;border:2px solid #cfe3ee;border-radius:3px;
  font-family:"Roboto Condensed",sans-serif;font-weight:400;font-size:25px;line-height:30px;color:#fff}
.toplinks{right:16px;top:19px;font-size:8px;color:#e4f0f6;display:flex;gap:6px;align-items:center}
.toplinks svg{width:13px;height:13px}

/* nav */
.navbar{left:76px;top:51px;width:644px;height:26px;background:linear-gradient(#f6f6f6,#dcdcdc);display:flex}
.navbar a{flex:1;font-size:7.6px;color:#444;display:flex;align-items:center;justify-content:center;border-left:1px solid #c9c9c9}
.navbar a.active{flex:0 0 109px;margin:4px 5px;background:var(--brand-deep);color:#fff;border:0;border-radius:2px}
.searchbar{left:82px;top:77px;width:631px;height:33px;background:var(--brand)}
.searchbar .field{position:absolute;top:9px;height:15px;font-size:7.6px;line-height:15px;padding-left:6px}
.city{left:10px;width:224px;background:var(--brand-deep);color:#e6f1f7}
.city svg{position:absolute;right:4px;top:2px;width:11px;height:11px}
.select{background:#fff;color:#555;border:1px solid #aaa}
.select::after{content:"";position:absolute;right:0;top:0;width:12px;height:13px;background:#ddd;border-left:1px solid #aaa}
.select i{position:absolute;right:3px;top:5px;border:3px solid transparent;border-top-color:#555;z-index:1}
.go{left:410px;width:43px;background:#1592c8;color:#fff;font-weight:700;text-align:center;padding:0;border:1px solid #bfe2f2}
.social{position:absolute;top:7px;width:19px;height:19px;border-radius:4px}

/* side menu */
.sidemenu{left:82px;top:139px;width:180px;height:161px;background:#fff;border:1px solid var(--line)}
.sidemenu h3{height:23px;background:var(--brand);color:#fff;font-size:8px;font-weight:700;line-height:23px;padding-left:12px}
.sidemenu li{list-style:none;font-size:7.6px;color:#666;height:19px;line-height:19px;padding-left:12px;border-bottom:1px solid #e6e6e6;position:relative}
.sidemenu li::before{content:"";position:absolute;left:5px;top:8px;width:3px;height:3px;border-radius:50%;background:#555}
.map{left:281px;top:139px;width:432px;height:161px;background:linear-gradient(135deg,#a9c6d8 0%,#c7d8c0 35%,#d9dcc6 55%,#b4cadb 80%);border:1px solid var(--line)}

/* headings */
.heading{font-family:"Roboto Condensed",sans-serif;font-weight:300;color:var(--brand);font-size:15px}

/* featured */
.featured{left:82px;top:344px;width:631px;height:160px;background:linear-gradient(#fff,#e8e8e8);border:1px solid var(--line)}
.card{position:absolute;top:10px;width:76px}
.card .thumb{height:74px;border:1px solid #e0e0e0;background:#fff;display:flex;align-items:center;justify-content:center}
.box-green{width:56px;height:40px;background:linear-gradient(135deg,#c6d98a,#93ae4a);border-radius:2px}
.box-tan{width:62px;height:46px;background:linear-gradient(135deg,#e3c98a,#b8914d);border-radius:2px}
.card .name{margin-top:11px;font-size:7.6px;font-weight:700;color:var(--link);line-height:10px}
.card .meta{margin-top:5px;font-size:7.6px;color:#333}
.card .row{margin-top:5px;font-size:7.6px;display:flex;justify-content:space-between;padding-right:4px}
.card .row u{color:#333}
.card .row b{color:#222}
.arrow{position:absolute;top:66px;width:30px;height:30px;border-radius:50%;background:linear-gradient(#fff,#ddd);border:1px solid #bbb}
.arrow svg{width:100%;height:100%}

/* sidebar panels */
.newsletter{left:82px;top:524px;width:180px;height:66px;background:var(--panel);border:1px solid #e2e2e2}
.newsletter .heading{position:absolute;left:13px;top:4px;font-size:13.5px}
.newsletter .email{position:absolute;left:13px;top:24px;width:155px;height:14px;background:#fff;border:1px solid #ccc;font-size:7.6px;font-style:italic;color:#999;line-height:12px;padding-left:8px}
.btn{position:absolute;background:var(--brand-deep);color:#fff;font-size:8px;font-weight:700;text-align:center;line-height:15px;border:1px solid #fff;outline:1px solid #9ab}
.quote{left:82px;top:610px;width:180px;height:51px;background:#e4e4e4}
.quote .tag{position:absolute;left:0;top:0;width:54px;height:51px;background:var(--brand);clip-path:polygon(0 0,78% 0,100% 50%,78% 100%,0 100%);color:#fff;font-family:"Roboto Condensed",sans-serif;font-weight:700;font-size:12px;line-height:16px;padding:8px 0 0 4px}
.quote .label{position:absolute;left:54px;top:8px;font-family:"Roboto Condensed",sans-serif;font-weight:400;font-size:14px;line-height:17px;color:#666;letter-spacing:.3px}
.quote .crate{position:absolute;right:8px;top:12px;width:34px;height:28px;background:linear-gradient(135deg,#e65d5d,#b02424)}
.panel{left:82px;width:180px;background:var(--panel)}
.panel h2{height:28px;background:var(--brand);color:#fff;font-family:"Roboto Condensed",sans-serif;font-weight:400;font-size:14px;text-align:center;line-height:28px}
.form-row{position:absolute;left:0;width:180px;height:14px}
.form-row span{position:absolute;right:113px;top:2px;font-size:7.6px;color:#555}
.form-row .input{position:absolute;left:73px;width:93px;height:14px;background:#fff;border:1px solid #d2d2d2}
.form-row .input.dd::after{content:"";position:absolute;right:0;top:0;width:12px;height:12px;border-left:1px solid #d2d2d2;background:#f2f2f2}
.form-row .input.dd i{position:absolute;right:3px;top:5px;border:3px solid transparent;border-top-color:#555;z-index:1}
.listing{position:absolute;left:11px;width:158px;font-size:6.5px;color:#555;border-bottom:1px dashed #d0d0d0;height:19px;line-height:19px;white-space:nowrap;overflow:hidden}

/* auctions */
.auction{left:281px;width:432px;height:102px;border-top:1px dashed #ccc}
.auction.shade{background:#eeeeee}
.auction .thumb{position:absolute;left:7px;top:8px;width:75px;height:80px;background:#fff;box-shadow:0 3px 4px rgba(0,0,0,.15);display:flex;align-items:center;justify-content:center}
.col{position:absolute;top:8px;font-size:7.4px;line-height:11.4px;color:#555}
.col h4{font-size:7.6px;font-weight:700;color:var(--link);line-height:10px;margin-bottom:3px}
.c1{left:89px;width:104px}
.c2{left:200px;width:70px}
.c3{left:283px;width:110px}
.c4{left:394px;width:40px}

/* footer */
.footnav{left:0;top:1106px;width:795px;height:36px;background:var(--brand);color:#fff;font-size:7.6px;line-height:36px;padding-left:83px;word-spacing:1px}
.footer{left:0;top:1142px;width:795px;height:58px;background:#e6e6e6}
.copy{left:83px;top:1152px;width:450px;font-size:7px;line-height:12px;color:#555}
.footbrand{left:549px;top:1151px;width:158px;height:36px;border:2px solid #7a7a7a;border-radius:3px;font-family:"Roboto Condensed",sans-serif;font-size:24px;line-height:31px;color:#666;text-align:center}
</style>
</head>
<body>
<div class="canvas">

  <header>
    <div class="abs masthead">
      <div class="abs brandname">cargolot.com</div>
      <div class="abs toplinks">
        <a href="#">Creat an Account</a>|<a href="#">Login</a>|<a href="#">About CargoLot.com</a>|<span>Contact Us:</span>
        <svg viewBox="0 0 16 16"><path d="M3 9V7a5 5 0 0 1 10 0v2" fill="none" stroke="#fff" stroke-width="1.6"/><rect x="2" y="8" width="3" height="5" rx="1" fill="#fff"/><rect x="11" y="8" width="3" height="5" rx="1" fill="#fff"/></svg>
        <span>555-014-2290</span>
      </div>
    </div>
    <nav class="abs navbar">
      <a class="active" href="#">20' Shipping Containers</a>
      <a href="#">40' Shipping Containers</a>
      <a href="#">40' High Cube Containers</a>
      <a href="#">Open Top Containers</a>
      <a href="#">How to Buy a Shipping Container</a>
    </nav>
    <div class="abs searchbar">
      <div class="field city">Search City, State or Country
        <svg viewBox="0 0 12 12"><circle cx="5" cy="5" r="3.5" fill="none" stroke="#fff" stroke-width="1.5"/><path d="M7.5 7.5 11 11" stroke="#fff" stroke-width="1.8"/></svg>
      </div>
      <div class="field select" style="left:246px;width:96px">Container Type<i></i></div>
      <div class="field select" style="left:354px;width:44px">Units<i></i></div>
      <div class="field go">Search</div>
      <span class="social" style="left:484px;background:#3b67b0"></span>
      <span class="social" style="left:511px;background:#3bb3e6"></span>
      <span class="social" style="left:538px;background:#2b8fc7"></span>
      <span class="social" style="left:565px;background:#444"></span>
      <span class="social" style="left:592px;background:#d2262a"></span>
    </div>
  </header>

  <aside class="abs sidemenu">
    <h3>How to Buy Shipping Containers</h3>
    <ul>
      <li>New Listings</li><li>News and Articles</li><li>About CargoLot.com</li>
      <li>Container Weights and Dimensions</li><li>CargoLot.com FAQs</li>
      <li>Shipping Container Terms</li><li>How to Sell Your Containers</li>
    </ul>
  </aside>
  <div class="abs map" role="img" aria-label="Map of North America with red pins marking container locations across the United States"></div>

  <h2 class="abs heading" style="left:84px;top:322px">Featured Shipping Containers for Sale</h2>
  <section class="abs featured">
    <div class="arrow" style="left:-16px"><svg viewBox="0 0 30 30"><path d="M18 8 11 15l7 7" fill="none" stroke="#aaa" stroke-width="2"/></svg></div>
    <div class="arrow" style="right:-16px"><svg viewBox="0 0 30 30"><path d="M12 8l7 7-7 7" fill="none" stroke="#aaa" stroke-width="2"/></svg></div>
    <div class="card" style="left:46px"><div class="thumb"><div class="box-green" role="img" aria-label="Green shipping container"></div></div><div class="name">Lorem Ipsum dolor dummy text</div><div class="meta">Container: XYZ</div><div class="row"><u>Location</u><b>$45600</b></div></div>
    <div class="card" style="left:160px"><div class="thumb"><div class="box-green" role="img" aria-label="Green shipping container"></div></div><div class="name">Lorem Ipsum dolor dummy text</div><div class="meta">Container: XYZ</div><div class="row"><u>Location</u><b>$45600</b></div></div>
    <div class="card" style="left:273px"><div class="thumb"><div class="box-green" role="img" aria-label="Green shipping container"></div></div><div class="name">Lorem Ipsum dolor dummy text</div><div class="meta">Container: XYZ</div><div class="row"><u>Location</u><b>$45600</b></div></div>
    <div class="card" style="left:387px"><div class="thumb"><div class="box-green" role="img" aria-label="Green shipping container"></div></div><div class="name">Lorem Ipsum dolor dummy text</div><div class="meta">Container: XYZ</div><div class="row"><u>Location</u><b>$45600</b></div></div>
    <div class="card" style="left:500px"><div class="thumb"><div class="box-green" role="img" aria-label="Green shipping container"></div></div><div class="name">Lorem Ipsum dolor dummy text</div><div class="meta">Container: XYZ</div><div class="row"><u>Location</u><b>$45600</b></div></div>
  </section>

  <div class="abs newsletter">
    <h3 class="heading">Subscribe to our Newsletter</h3>
    <div class="email">Enter Email Address</div>
    <div class="btn" style="left:13px;top:46px;width:48px">Subscribe</div>
  </div>

  <div class="abs quote">
    <div class="tag">FAST<br>QUOTE</div>
    <div class="label">CONTAINER<br>QUOTE</div>
    <div class="crate" role="img" aria-label="Red shipping container"></div>
  </div>

  <section class="abs panel" style="top:682px;height:211px">
    <h2>Advanced Search</h2>
    <div class="form-row" style="top:35px"><span>Listing Type</span><div class="input dd"><i></i></div></div>
    <div class="form-row" style="top:54px"><span>Container Type</span><div class="input dd"><i></i></div></div>
    <div class="form-row" style="top:73px"><span>Listing Number</span><div class="input"></div></div>
    <div class="form-row" style="top:92px"><span>Location</span><div class="input"></div></div>
    <div class="form-row" style="top:111px"><span>Distance From</span><div class="input dd"><i></i></div></div>
    <div class="form-row" style="top:130px"><span>ISO Code</span><div class="input"></div></div>
    <div class="form-row" style="top:149px"><span>BIC Sode</span><div class="input"></div></div>
    <div class="form-row" style="top:168px"><span>Condition / Age</span><div class="input dd"><i></i></div></div>
    <div class="btn" style="left:73px;top:189px;width:48px">Search</div>
  </section>

  <section class="abs panel" style="top:915px;height:161px">
    <h2>Latest Listings</h2>
    <div class="listing" style="top:33px">2853 - 40' high cube container - ASIS - Miami, FL</div>
    <div class="listing" style="top:52px">2846 - 20' storage unit, water tight - Denver, CO</div>
    <div class="listing" style="top:71px">2845 - 20' shipping/storage container - Denver, CO</div>
    <div class="listing" style="top:90px">2844 - 40' storage container - Cleveland, OH</div>
    <div class="listing" style="top:109px">2843 - 40' shipping container, CW, at the depot -</div>
    <div class="listing" style="top:128px;border:0">2853 - 40' high cube container - ASIS - Miami, FL</div>
  </section>

  <h2 class="abs heading" style="left:283px;top:524px">Shipping Container Auctions Closing Soon</h2>

  <div class="abs auction shade" style="top:564px">
    <div class="thumb"><div class="box-tan" role="img" aria-label="Tan shipping container"></div></div>
    <div class="col c1"><h4>Lorem Ipsum dolor dummy text</h4>Lorem ipsum dolor sit amet, consectetur adipiscing elit. Mauris quis lacinia diam. Vestibulum ac tortor porta velit faucibus pulvinar.</div>
    <div class="col c2"><h4>Container Type</h4>Lorem ipsum dolor.</div>
    <div class="col c3"><h4>Location</h4>Lorem ipsum dolor sit amet</div>
    <div class="col c4"><h4>Price</h4>$ 45600</div>
  </div>
  <div class="abs auction" style="top:666px">
    <div class="thumb"><div class="box-tan" role="img" aria-label="Tan shipping container"></div></div>
    <div class="col c1"><h4>Lorem Ipsum dolor dummy text</h4>Lorem ipsum dolor sit amet, consectetur adipiscing elit. Mauris quis lacinia diam. Vestibulum ac tortor porta velit faucibus pulvinar.</div>
    <div class="col c2"><h4>Container Type</h4>Lorem ipsum dolor.</div>
    <div class="col c3"><h4>Location</h4>Lorem ipsum dolor sit amet</div>
    <div class="col c4"><h4>Price</h4>$ 45600</div>
  </div>
  <div class="abs auction shade" style="top:767px">
    <div class="thumb"><div class="box-tan" role="img" aria-label="Tan shipping container"></div></div>
    <div class="col c1"><h4>Lorem Ipsum dolor dummy text</h4>Lorem ipsum dolor sit amet, consectetur adipiscing elit. Mauris quis lacinia diam. Vestibulum ac tortor porta velit faucibus pulvinar.</div>
    <div class="col c2"><h4>Container Type</h4>Lorem ipsum dolor.</div>
    <div class="col c3"><h4>Location</h4>Lorem ipsum dolor sit amet</div>
    <div class="col c4"><h4>Price</h4>$ 45600</div>
  </div>
  <div class="abs auction" style="top:869px">
    <div class="thumb"><div class="box-tan" role="img" aria-label="Tan shipping container"></div></div>
    <div class="col c1"><h4>Lorem Ipsum dolor dummy text</h4>Lorem ipsum dolor sit amet, consectetur adipiscing elit. Mauris quis lacinia diam. Vestibulum ac tortor porta velit faucibus pulvinar.</div>
    <div class="col c2"><h4>Container Type</h4>Lorem ipsum dolor.</div>
    <div class="col c3"><h4>Location</h4>Lorem ipsum dolor sit amet</div>
    <div class="col c4"><h4>Price</h4>$ 45600</div>
  </div>
  <div class="abs auction shade" style="top:970px;border-bottom:1px dashed #ccc">
    <div class="thumb"><div class="box-tan" role="img" aria-label="Tan shipping container"></div></div>
    <div class="col c1"><h4>Lorem Ipsum dolor dummy text</h4>Lorem ipsum dolor sit amet, consectetur adipiscing elit. Mauris quis lacinia diam. Vestibulum ac tortor porta velit faucibus pulvinar.</div>
    <div class="col c2"><h4>Container Type</h4>Lorem ipsum dolor.</div>
    <div class="col c3"><h4>Location</h4>Lorem ipsum dolor sit amet</div>
    <div class="col c4"><h4>Price</h4>$ 45600</div>
  </div>

  <footer>
    <nav class="abs footnav">Privacy Policy &nbsp;| &nbsp;User Agreement &nbsp;| &nbsp;About CargoLot &nbsp;| &nbsp;News &nbsp;| &nbsp;Glossary &nbsp;| &nbsp;Dimensions &amp; ISO Codes &nbsp;| &nbsp;Faq &nbsp;| &nbsp;Help &nbsp;| &nbsp;Contact &nbsp;| &nbsp;Browse By Area</nav>
    <div class="abs footer"></div>
    <p class="abs copy">Copyright © 2011-2013 CargoLot, Inc. All Rights Reserved. CargoLot.com is a trademark of CargoLot Inc. Designated trademarks and brands are the property of their respective owners. Use of this Web site constitutes acceptance of the CargoLot user agreement and privacy policy.</p>
    <div class="abs footbrand">cargolot.com</div>
  </footer>

</div>
</body>
</html>
```